cover design for presentation folder

I am looking for a simple cover design for a 9X12 folder cover. I want our logo featured and some design element from our logo incorporated. I have attached two versions on our logo.

Colors

Designer to choose colors to be used in the design.

```html
<!DOCTYPE html>
<html lang="en">
<head>
<meta charset="utf-8">
<title>Presentation Folder Cover</title>
<link href="https://fonts.googleapis.com/css2?family=Open+Sans:wght@700&display=swap" rel="stylesheet">
<style>
  :root {
    --backdrop: #d9d9d9;
    --green-deep: #00703c;
    --green-mid: #0f7a3e;
    --green-bright: #1e8c41;
    --gold: #fbb017;
    --indigo: #2e3092;
    --paper: #ffffff;
  }
  html, body {
    margin: 0;
    padding: 0;
    width: 1200px;
    height: 847px;
    overflow: hidden;
    background: var(--backdrop);
  }
  .folder-spread {
    position: absolute;
    left: 60px;
    top: 63px;
    width: 1080px;
    height: 720px;
    display: flex;
    box-shadow: 0 18px 40px rgba(0,0,0,0.25);
  }
  .folder-panel {
    position: relative;
    width: 540px;
    height: 720px;
    overflow: hidden;
  }
  .folder-panel svg {
    position: absolute;
    inset: 0;
    display: block;
  }
  .anniversary-mark {
    position: absolute;
    left: 120px;
    top: 92px;
    display: flex;
    align-items: center;
    gap: 10px;
    font-family: "Open Sans", sans-serif;
    font-weight: 700;
    font-size: 19px;
    line-height: 1.1;
    color: var(--paper);
  }
  .anniversary-mark .dot {
    width: 22px;
    height: 22px;
    border-radius: 50%;
    background: var(--paper);
    flex: none;
  }
  .brand-lockup {
    position: absolute;
    right: 34px;
    top: 582px;
    display: flex;
    align-items: center;
    gap: 12px;
    font-family: "Open Sans", sans-serif;
    font-weight: 700;
    font-size: 21px;
    line-height: 1.1;
    letter-spacing: -0.3px;
    color: var(--indigo);
    text-transform: uppercase;
  }
  .brand-lockup .square {
    width: 44px;
    height: 44px;
    background: var(--indigo);
    flex: none;
  }
</style>
</head>
<body>
  <main class="folder-spread">
    <section class="folder-panel back-cover" aria-label="Back cover">
      <svg width="540" height="720" viewBox="0 0 540 720" aria-hidden="true">
        <defs>
          <linearGradient id="back-green" x1="0" y1="0" x2="1" y2="0">
            <stop offset="0" stop-color="var(--green-deep)"/>
            <stop offset="0.6" stop-color="var(--green-mid)"/>
            <stop offset="1" stop-color="#136a36"/>
          </linearGradient>
        </defs>
        <rect class="field" width="540" height="720" fill="url(#back-green)"/>
        <path class="gold-band" d="M0,310 Q140,515 285,720 L150,720 Q72,618 0,520 Z" fill="var(--gold)"/>
        <path class="indigo-corner" d="M0,520 Q72,618 150,720 L0,720 Z" fill="var(--indigo)"/>
      </svg>
    </section>

    <section class="folder-panel front-cover" aria-label="Front cover">
      <svg width="540" height="720" viewBox="0 0 540 720" aria-hidden="true">
        <rect class="field" width="540" height="720" fill="var(--paper)"/>
        <path class="green-wedge" d="M0,0 L335,0 Q175,330 0,690 Z" fill="var(--green-bright)"/>
        <path class="gold-band" d="M335,0 L415,0 Q235,375 70,720 L0,720 L0,690 Q175,330 335,0 Z" fill="var(--gold)"/>
      </svg>

      <div class="anniversary-mark">
        <span class="dot"></span>
        <span>Fifty Years<br>of Giving</span>
      </div>

      <div class="brand-lockup">
        <span class="square"></span>
        <span>Ridgeline Valley<br>Community Fund</span>
      </div>
    </section>
  </main>
</body>
</html>
```